Corvimo Business Card

Corvimo is a young and energetic software development consultancy. We spend our time on the road working with clients on their sites an meeting new potential customers and employees!

We need a sharp, vibrant and memorable business card that will inspires those that receive it to look after it as it oozes quality and is a nice thing in its own right.

We like bold colours and distinctive design. So show us what you can do.

In terms of information on the card, it would be good to see:

* Our logo (Obviously :) )
* Employee name
* Email
* Website address
* Mobile number
* Full company name (Corvimo ltd)
* Registered company number
* Registered company address

Industry/Entity Type

Software

Requirements
Nice to have
• We are thinking that having a QR Code on the business card could be a good way of adding active marketing. It would be good to see if you are able to merge the kind of element in to your designs!

Maybe something special could be achieved using a visual QR Code like those produced at http://www.pixoranta.example/ ? You have our media so feel free to have a play.

```html
<!DOCTYPE html>
<html lang="en">
<head>
<meta charset="utf-8">
<title>Corvimo Business Card</title>
<link rel="stylesheet" href="https://fonts.googleapis.com/css2?family=Exo+2:wght@300;400;500&display=swap">
<style>
  :root {
    --brand-red: #c1202e;
    --paper-white: #ffffff;
    --backdrop: #d9dadc;
    --ink-light: #fbe9ea;
  }
  * { margin: 0; padding: 0; box-sizing: border-box; }
  html, body {
    width: 1200px; height: 900px; overflow: hidden;
    background: var(--backdrop);
    font-family: "Exo 2", Arial, sans-serif;
  }
  .canvas { position: relative; width: 1200px; height: 900px; }

  .card {
    position: absolute;
    width: 560px; height: 320px;
    overflow: hidden;
    box-shadow: 0 6px 18px rgba(0,0,0,0.18);
  }

  /* Back of card */
  .card-back {
    left: 560px; top: 90px;
    background: var(--brand-red);
  }
  .card-back .pattern-area {
    position: absolute; inset: 0;
    background: linear-gradient(135deg, #c72634 0%, #b81c2a 100%);
  }

  /* Front of card */
  .card-front {
    left: 80px; top: 470px;
    background: var(--paper-white);
  }
  .front-header {
    position: absolute; left: 0; top: 0; width: 100%; height: 140px;
  }
  .brand-name {
    position: absolute; left: 40px; top: 52px;
    font-weight: 300; font-size: 58px; letter-spacing: 3px;
    color: var(--brand-red);
    line-height: 1;
  }
  .front-body {
    position: absolute; left: 0; top: 140px; width: 100%; height: 180px;
    background: var(--brand-red);
  }
  .band-line {
    position: absolute; left: 0; top: 10px; width: 100%; height: 2px;
    background: var(--paper-white);
  }
  .identity {
    position: absolute; left: 40px; top: 36px;
    display: flex; align-items: center; gap: 12px;
    color: var(--paper-white); white-space: nowrap;
  }
  .person-name { font-size: 16px; font-weight: 500; letter-spacing: 1.5px; }
  .person-role {
    font-size: 10.5px; letter-spacing: 1.2px; color: var(--ink-light);
    padding-left: 12px; border-left: 1px solid var(--ink-light);
    line-height: 14px;
  }
  .contact-list {
    position: absolute; left: 40px; top: 82px; list-style: none;
    color: var(--ink-light); font-size: 12px; letter-spacing: 1px;
    white-space: nowrap;
  }
  .contact-list li { display: flex; align-items: center; gap: 10px; height: 24px; }
  .contact-list svg { width: 14px; height: 14px; flex: none; }
  .divider {
    position: absolute; left: 346px; top: 36px; width: 1px; height: 100px;
    background: var(--ink-light); opacity: 0.8;
  }
  .address {
    position: absolute; left: 360px; top: 34px;
    font-style: normal; color: var(--ink-light);
    font-size: 10.5px; line-height: 1.9; letter-spacing: 0.8px;
    white-space: nowrap;
  }
</style>
</head>
<body>
<main class="canvas">

  <section class="card card-back" aria-label="Card back">
    <div class="pattern-area" role="img" aria-label="Repeating brand-name pattern in white on red"></div>
  </section>

  <section class="card card-front" aria-label="Card front">
    <header class="front-header">
      <div class="brand-name">CORVIMO</div>
    </header>
    <div class="front-body">
      <div class="band-line"></div>
      <div class="identity">
        <span class="person-name">MARTEN HALVORSEN</span>
        <span class="person-role">CONSULTANT</span>
      </div>
      <ul class="contact-list">
        <li>
          <svg viewBox="0 0 14 14" fill="none" stroke="#fbe9ea" stroke-width="1.3"><rect x="3.5" y="1" width="7" height="12" rx="1.2"/><line x1="6" y1="11" x2="8" y2="11"/></svg>
          +00 555 XX XXX
        </li>
        <li>
          <svg viewBox="0 0 14 14" fill="none" stroke="#fbe9ea" stroke-width="1.3"><rect x="1" y="3" width="12" height="8"/><polyline points="1,3 7,8 13,3"/></svg>
          HALVORSEN@CORVIMOSOFT.EXAMPLE
        </li>
        <li>
          <svg viewBox="0 0 14 14" fill="none" stroke="#fbe9ea" stroke-width="1.2"><circle cx="7" cy="7" r="5.8"/><ellipse cx="7" cy="7" rx="2.6" ry="5.8"/><line x1="1.2" y1="7" x2="12.8" y2="7"/></svg>
          WWW.CORVIMOSOFT.EXAMPLE
        </li>
      </ul>
      <div class="divider"></div>
      <address class="address">
        NORDVIK ADDRESS AT, PO BOX XX,<br>
        XXXX VESTHOLM,<br>
        NORVELAND
      </address>
    </div>
  </section>

</main>
</body>
</html>
```